Maple Sprout Menu (Vegetarian Restaurant Concept)

Maple Sprout is a new concept fast casual restaurant
renders are attached so you can see the style of restaurant
Maple Sprowt is a vibrant and modern Vegetarian fast casual restaurant concept that mixes fresh food, energy, great décor, and a comfortable, welcoming atmosphere to provide a memorable and all Vegetarian dining experience.
Our Mission is to be top of mind when consumers think Vegetarian food!
Target Market(s)
the menu is vegetarian and appeals to a broad demographic in USA
Colors
Designer to choose colors to be used in the design.
Requirements
Must have
- well colored and well laid out menu - should not be cartoonish
Nice to have
- For Phots please use the shots in this file:
- https://www.filecrate-example.net/sh/kq7trm2wzl4pnad/BBBxT_qPwLdRNVoE_KMS_Tb?dl=0
- note these are untouched and you are free to change as needed
Should not have
- Should not be cartoonish - nor kives, forks etc in the design

```html
<!DOCTYPE html>
<html lang="en">
<head>
<meta charset="utf-8">
<title>Maple Sprout Menu</title>
<link href="https://fonts.googleapis.com/css2?family=Abril+Fatface&display=swap" rel="stylesheet">
<style>
  :root {
    --paper: #ffffff;
    --panel: #212427;
    --ink: #ffffff;
    --leaf: #5f9e3c;
    --bun: #c99a6a;
    --patty: #6b4128;
    --berry: #c8303a;
    --dish: #e9e6e3;
  }
  * { margin: 0; padding: 0; box-sizing: border-box; }
  html, body {
    width: 848px; height: 1200px; overflow: hidden;
    background: var(--paper);
  }
  .menu {
    position: relative; width: 848px; height: 1200px;
    background: var(--paper); overflow: hidden;
    font-family: "Abril Fatface", Georgia, serif;
  }
  .photo-strip {
    position: absolute; left: 0; top: 0; width: 299px; height: 1200px;
  }
  .panel {
    position: absolute; left: 299px; top: 0; width: 549px; height: 1200px;
    background: var(--panel);
  }
  .rule {
    position: absolute; left: 342px; width: 464px; height: 2px;
    background: var(--ink);
  }
  .copy {
    position: absolute; left: 344px; top: 0; width: 592px; height: 1200px;
    transform: scaleX(0.78); transform-origin: left top;
    color: var(--ink);
  }
  .copy > * { position: absolute; left: 0; white-space: nowrap; }
  .section-title {
    font-size: 53px; line-height: 55px; font-weight: 400; letter-spacing: 0.5px;
  }
  .dish {
    font-size: 30px; line-height: 32px; font-weight: 400;
  }
  .dish-notes {
    font-size: 19px; line-height: 21.5px; color: var(--leaf);
  }
</style>
</head>
<body>
<main class="menu">
  <svg class="photo-strip" viewBox="0 0 299 1200" role="img" aria-label="Photos of a stacked veggie burger and a strawberry coconut fruit bowl">
    <defs>
      <radialGradient id="burger-tone" cx="0.1" cy="0.5" r="0.7">
        <stop offset="0" stop-color="#8a5a37"/>
        <stop offset="0.45" stop-color="var(--patty)"/>
        <stop offset="0.75" stop-color="var(--bun)"/>
        <stop offset="1" stop-color="#d9b58e"/>
      </radialGradient>
      <radialGradient id="bowl-tone" cx="0.1" cy="0.45" r="0.7">
        <stop offset="0" stop-color="#7a3a40"/>
        <stop offset="0.6" stop-color="#a8343c"/>
        <stop offset="0.85" stop-color="var(--berry)"/>
        <stop offset="0.93" stop-color="var(--dish)"/>
      </radialGradient>
    </defs>
    <circle cx="16" cy="312" r="242" fill="url(#burger-tone)"/>
    <circle cx="17" cy="891" r="240" fill="url(#bowl-tone)"/>
  </svg>

  <div class="panel"></div>

  <div class="rule" style="top:143px"></div>
  <div class="rule" style="top:680px"></div>
  <div class="rule" style="top:998px"></div>

  <div class="copy">
    <h1 class="section-title" style="top:33px">BURGERS, WRAPS<br>&amp; SANDWICHES</h1>

    <p class="dish" style="top:184px">Sweet Potato, Black Bean Veggie<br>Burgers with Cabbage Pepita Slaw</p>
    <p class="dish" style="top:266px">Roasted Vejjie, Arugula<br>and Hummus Wraps</p>
    <p class="dish" style="top:347px">Garden Burger</p>
    <p class="dish" style="top:397px">Beans and Greens Quesadillas</p>
    <p class="dish-notes" style="top:439px">greens, Mexican cheese, beans and avocado, with salsa</p>
    <p class="dish" style="top:475px">Vejjie Burrito</p>
    <p class="dish-notes" style="top:517px">greens, Mexican cheese, beans, brown rice,<br>roasted chili corn and avocado, with ancho<br>chili salsa, wheat tortilla</p>

    <h2 class="section-title" style="top:624px">BOWLS</h2>
    <p class="dish" style="top:717px">Roasted Vegetable, and Spinach Bowl</p>
    <p class="dish" style="top:765px">Sugar Snap Pea and Carrot Soba Noodles</p>
    <p class="dish" style="top:815px">Whole Grain and Vegetable Buddha Bowl</p>
    <p class="dish" style="top:864px">Orange and Pistacio Quinoa</p>

    <h2 class="section-title" style="top:941px">DESSERT</h2>
    <p class="dish" style="top:1041px">Strawberry Balsamic Ice Cream Sundae</p>
    <p class="dish" style="top:1089px">Exotic Fruit Bowl</p>
    <p class="dish" style="top:1137px">White and Dark Oatmeal Cookie</p>
  </div>
</main>
</body>
</html>
```